tilebaron.org needs a cool website!

I need a website designed for a commercial flooring maintenance company based in Texas. We will be providing services like carpet shampooing, burnishing, resurfacing and power washing. It needs to be cool and trendy.

I’ll need 10-20 pages. I need help deciding on the style and color palette. We will need great stock pictures of different flooring types and you will need to photo shop our logo on imaginary cars or storefronts.

Please have similar experience and an open mind. I’m looking for a partnership and someone to turn to for future projects and upkeep.

The domain is currently hosted on Wix. You will need the ability to develop and code it there.
Updates

Target Market(s)

Commercial businesses and properties

Industry/Entity Type

Floor care

Coding

Coded - Design and coding required

Number of Pages Required

5+ page

Requirements
Must have
• Great pictures of different types of floors.

```html
<!DOCTYPE html>
<html lang="en">
<head>
<meta charset="utf-8">
<title>tilebaron — Commercial Floor Care in Texas</title>
<link rel="stylesheet" href="https://fonts.googleapis.com/css2?family=Plus+Jakarta+Sans:wght@400;500;600;700&display=swap">
<style>
:root{
  --green:#1db45a;
  --green-soft:#e8f7ee;
  --ink:#121212;
  --muted:#7a7a7a;
  --line:#e6e6e6;
  --card:#f6f6f7;
  --blue:#2a3fd1;
  --white:#fff;
}
*{box-sizing:border-box;margin:0;padding:0}
html,body{width:1200px;height:5338px;overflow:hidden;background:var(--white)}
body{font-family:"Plus Jakarta Sans",sans-serif;color:var(--ink);position:relative}
.abs{position:absolute}
.btn{display:inline-flex;align-items:center;gap:6px;border-radius:6px;font-size:13px;font-weight:500}
.btn-green{background:var(--green);color:#fff}
.btn-out{border:1px solid var(--line);color:var(--ink);background:#fff}
.eyebrow{color:var(--green);font-size:11px;text-align:center;width:1200px;left:0}
.section-title{font-size:38px;font-weight:500;text-align:center;width:1200px;left:0;letter-spacing:-.5px}
.section-sub{font-size:12.5px;color:var(--muted);text-align:center;line-height:20px}
.photo{border-radius:4px}

/* header */
.logo{font-size:26px;font-weight:500;display:flex;align-items:center;gap:8px}
.logo .dot{width:12px;height:12px;border-radius:50%;background:var(--green)}
.nav{display:flex;gap:22px;font-size:12px}
.nav .active{color:var(--green)}

/* hero */
.pill{border:1px solid var(--green);color:var(--green);border-radius:20px;font-size:11px;padding:4px 10px}
.hero-title{font-size:64px;font-weight:500;line-height:74px;letter-spacing:-1px}
.hero-text{font-size:12.5px;color:var(--muted);line-height:20px;width:430px}

/* features */
.feature{display:flex;gap:22px;width:420px}
.feature .ico{flex:none;width:46px;height:46px;border-radius:8px;background:var(--green);display:flex;align-items:center;justify-content:center}
.feature h3{font-size:19px;font-weight:500;margin:2px 0 8px}
.feature p{font-size:12px;color:var(--muted);line-height:20px}

/* service cards */
.svc{background:var(--card);border-radius:10px;width:452px;height:312px;padding:20px}
.svc .thumb{width:124px;height:124px;border-radius:4px}
.svc h3{font-size:19px;font-weight:500;margin:32px 0 14px}
.svc p{font-size:12px;color:var(--muted);line-height:20px;width:400px}
.svc .more{font-size:11px;margin-top:14px;display:flex;align-items:center;gap:6px}
.svc .more.blue{color:var(--blue)}

/* testimonials */
.stars{display:flex;gap:4px}
.person{background:#fff;border-radius:6px;display:flex;align-items:center;gap:12px;padding:12px 16px}
.avatar{width:44px;height:44px;border-radius:4px;background:linear-gradient(135deg,#c9b8a8,#6b5a4d)}
.person b{font-size:13px;font-weight:500;display:block}
.person small{font-size:10px;color:var(--muted)}
.dots{display:flex;gap:6px;left:0;width:1200px;justify-content:center}
.dots span{width:34px;height:3px;background:#e4e4e8;border-radius:2px}
.dots span.on{background:var(--blue)}

/* team */
.member{border:1px solid var(--line);border-radius:10px;background:#fff;padding:24px;display:flex;gap:24px}
.member .pic{flex:none;width:168px;height:185px;border-radius:4px}
.member h3{font-size:20px;font-weight:500}
.member .role{font-size:12px;color:var(--muted);margin:2px 0 14px}
.member p{font-size:12px;color:var(--muted);line-height:20px}
.socials{display:flex;gap:8px;margin-top:14px}
.socials span{width:20px;height:20px;border:1px solid #444;border-radius:50%}

/* stats */
.stat{text-align:center;width:320px}
.stat b{font-size:40px;font-weight:500;display:block}
.stat span{font-size:14px;color:var(--muted)}
.vline{width:2px;height:96px;background:var(--blue)}

/* form */
.form{background:var(--card);border-radius:14px}
.field label{font-size:13px;display:block;margin-bottom:12px}
.field .input{background:#fff;border:1px solid var(--line);border-radius:5px;height:38px;font-size:11px;color:var(--muted);padding:12px 10px}

/* footer */
.foot-col h4{font-size:16px;font-weight:500;margin-bottom:24px}
.foot-col li{list-style:none;font-size:12px;color:var(--muted);margin-bottom:18px;display:flex;align-items:center;gap:10px}
</style>
</head>
<body>

<!-- Header -->
<header>
  <div class="logo abs" style="left:138px;top:30px">tilebaron<span class="dot"></span></div>
  <nav class="nav abs" style="left:710px;top:40px">
    <span class="active">Home</span><span>About Us</span><span>Services</span><span>Gallery</span>
  </nav>
  <span class="btn btn-green abs" style="left:972px;top:30px;padding:10px 14px">Contact Us</span>
</header>

<!-- Hero -->
<section class="hero">
  <span class="pill abs" style="left:135px;top:205px">Texas' Premier Commercial Flooring Maintenance</span>
  <h1 class="hero-title abs" style="left:135px;top:236px">Keeping Your<br>Business Floors<br>Pristine</h1>
  <p class="hero-text abs" style="left:135px;top:476px">From carpet shampooing to power washing, we provide expert floor care services tailored to commercial properties</p>
  <p class="hero-text abs" style="left:135px;top:530px">Trusted by businesses across Texas, we bring years of experience and state-of-the-art cleaning techniques to extend the life and beauty of your flooring</p>
  <span class="btn btn-green abs" style="left:135px;top:616px;padding:10px 14px">Contact Us</span>
  <span class="btn btn-out abs" style="left:240px;top:616px;padding:9px 12px">Learn more
    <svg width="12" height="10" viewBox="0 0 12 10"><path d="M1 5h10M7 1l4 4-4 4" stroke="#121212" fill="none" stroke-width="1.3"/></svg></span>
  <div class="abs" role="img" aria-label="Worker in blue overalls running a yellow floor burnisher across a glossy office floor" style="left:613px;top:135px;width:587px;height:583px;background:linear-gradient(160deg,#d7e3ef 0%,#8fa7bd 45%,#3e5064 75%,#c9a83a 100%)"></div>
</section>

<!-- Why choose us -->
<section class="why">
  <p class="eyebrow abs" style="top:804px">Why Choose Us</p>
  <h2 class="section-title abs" style="top:824px">Why Choose Us for Your Flooring Maintenance?</h2>
  <p class="section-sub abs" style="left:140px;top:890px;width:920px">Our team of skilled technicians is dedicated to providing comprehensive floor care services that help maintain the cleanliness and safety of your commercial space. Whether it's carpet shampooing, resurfacing, or power washing, we use cutting-edge equipment and eco-friendly products to ensure top-notch results every time.</p>

  <div class="feature abs" style="left:115px;top:988px">
    <div class="ico"><svg width="22" height="22" viewBox="0 0 24 24" fill="none" stroke="#fff" stroke-width="1.6"><path d="M12 3v4M12 17v4M3 12h4M17 12h4M6 6l2.5 2.5M15.5 15.5L18 18M6 18l2.5-2.5M15.5 8.5L18 6"/></svg></div>
    <div><h3>Customized Service</h3><p>We understand that every business is different. Our flexible service packages are designed to accommodate your unique flooring needs</p></div>
  </div>
  <div class="feature abs" style="left:115px;top:1102px">
    <div class="ico"><svg width="22" height="22" viewBox="0 0 24 24" fill="none" stroke="#fff" stroke-width="1.6"><circle cx="12" cy="9" r="3.5"/><path d="M5 20c1-4 4-6 7-6s6 2 7 6z"/></svg></div>
    <div><h3>Texas-Focused Expertise</h3><p>As a locally owned company, we know the specific challenges of maintaining commercial floors in Texas. From extreme weather to high foot traffic, we tailor our services to keep your floors in peak condition.</p></div>
  </div>
  <div class="feature abs" style="left:115px;top:1236px">
    <div class="ico"><svg width="22" height="22" viewBox="0 0 24 24" fill="none" stroke="#fff" stroke-width="1.6"><rect x="3" y="7" width="18" height="13" rx="2"/><path d="M9 7V4h6v3M3 12h18"/></svg></div>
    <div><h3>State-of-the-Art Equipment</h3><p>We invest in the latest cleaning technology and use environmentally friendly products, delivering results that are both highly effective and sustainable for your business</p></div>
  </div>
  <div class="feature abs" style="left:115px;top:1370px">
    <div class="ico"><svg width="22" height="22" viewBox="0 0 24 24" fill="none" stroke="#fff" stroke-width="1.6"><path d="M12 3l8 3v6c0 5-4 8-8 9-4-1-8-4-8-9V6z"/><path d="M8.5 12l2.5 2.5 4.5-5"/></svg></div>
    <div><h3>Certified, Licensed, and Insured</h3><p>Self-defence is not just about physical techniques: In today's world, knowing how to protect yourself.</p></div>
  </div>
  <div class="abs photo" role="img" aria-label="Floor scrubbing machine in a bright office with tall windows" style="left:596px;top:990px;width:486px;height:452px;border-radius:10px;background:linear-gradient(170deg,#eef1f3 0%,#b9c4cb 50%,#6f7b83 80%,#d6d9db 100%)"></div>
</section>

<!-- Services -->
<section class="services">
  <p class="eyebrow abs" style="top:1546px">Services</p>
  <h2 class="section-title abs" style="top:1566px">Surpassing Standards for Outstanding Success</h2>
  <p class="section-sub abs" style="left:210px;top:1632px;width:780px">Define ambitious service benchmarks that challenge your team to strive for excellence. These benchmarks should be both aspirational and achievable, inspiring everyone to aim higher and constantly improve.</p>

  <div class="svc abs" style="left:133px;top:1712px">
    <div class="thumb" role="img" aria-label="Carpet shampooing machine on blue carpet" style="background:linear-gradient(140deg,#c9a23a,#3b6aa8 60%,#1f3f6e)"></div>
    <h3>Carpet Shampooing</h3>
    <p>Deep cleaning that removes dirt, stains, and allergens from high-traffic areas.</p>
    <div class="more">Read More <svg width="12" height="10" viewBox="0 0 12 10"><path d="M1 5h10M7 1l4 4-4 4" stroke="currentColor" fill="none" stroke-width="1.3"/></svg></div>
  </div>
  <div class="svc abs" style="left:613px;top:1712px">
    <div class="thumb" role="img" aria-label="Grinder throwing sparks while polishing a hard floor" style="background:linear-gradient(140deg,#2c2a2a,#7a4a24 55%,#e08a2e)"></div>
    <h3>Burnishing and Polishing</h3>
    <p>Restore shine and eliminate scuff marks to keep your hard floors looking new</p>
    <div class="more blue">Read More <svg width="12" height="10" viewBox="0 0 12 10"><path d="M1 5h10M7 1l4 4-4 4" stroke="currentColor" fill="none" stroke-width="1.3"/></svg></div>
  </div>
  <div class="svc abs" style="left:133px;top:2052px">
    <div class="thumb" role="img" aria-label="Freshly resurfaced wooden floor" style="background:linear-gradient(150deg,#3a2418,#a35a2a 55%,#d99a5c)"></div>
    <h3>Floor Resurfacing</h3>
    <p>Extend the life of your floors with our professional resurfacing solutions</p>
    <div class="more blue">Read More <svg width="12" height="10" viewBox="0 0 12 10"><path d="M1 5h10M7 1l4 4-4 4" stroke="currentColor" fill="none" stroke-width="1.3"/></svg></div>
  </div>
  <div class="svc abs" style="left:613px;top:2052px">
    <div class="thumb" role="img" aria-label="Power washing an outdoor paved area" style="background:linear-gradient(150deg,#7d8f5a,#9aa3a6 55%,#5b6570)"></div>
    <h3>Power Washing</h3>
    <p>Remove grime and buildup from outdoor areas to enhance the exterior appeal of your property</p>
    <div class="more blue">Read More <svg width="12" height="10" viewBox="0 0 12 10"><path d="M1 5h10M7 1l4 4-4 4" stroke="currentColor" fill="none" stroke-width="1.3"/></svg></div>
  </div>

  <div class="abs" style="left:133px;top:2405px;width:933px;height:276px;background:var(--card);border-radius:10px"></div>
  <div class="abs" role="img" aria-label="Mop cleaning brown ceramic tile grout lines" style="left:166px;top:2437px;width:214px;height:210px;border-radius:10px;background:linear-gradient(140deg,#3b2a20,#8a5a36 50%,#c99868)"></div>
  <h3 class="abs" style="left:406px;top:2490px;font-size:19px;font-weight:500">Tile , Grout Cleaning and more !</h3>
  <p class="abs" style="left:406px;top:2532px;font-size:12px;color:var(--muted)">Thoroughly clean and disinfect your tile floors for a fresh and hygienic finish</p>
  <span class="btn btn-out abs" style="left:406px;top:2566px;padding:8px 16px;font-size:11px;color:var(--green)">Discover More Services
    <svg width="12" height="10" viewBox="0 0 12 10"><path d="M1 5h10M7 1l4 4-4 4" stroke="currentColor" fill="none" stroke-width="1.3"/></svg></span>
</section>

<!-- Testimonials -->
<section class="testimonials">
  <p class="eyebrow abs" style="top:2767px">Testimonial</p>
  <h2 class="section-title abs" style="top:2787px">Experiences Shared by Our Clients</h2>

  <div class="abs" style="left:133px;top:2877px;width:294px;height:328px;background:var(--card)"></div>
  <div class="stars abs" style="left:160px;top:2903px">
    <svg width="100" height="16" viewBox="0 0 100 16"><g fill="#f5b400"><path id="st" d="M8 1l2 5h5l-4 3 1.6 5L8 11l-4.6 3L5 9 1 6h5z"/><use href="#st" x="20"/><use href="#st" x="40"/><use href="#st" x="60"/><use href="#st" x="80"/></g></svg>
  </div>
  <p class="abs" style="left:160px;top:2938px;width:240px;font-size:12px;line-height:19px">Their floor resurfacing service saved us thousands in replacement costs. Highly recommended!</p>
  <div class="person abs" style="left:160px;top:3100px;width:240px">
    <div class="avatar" role="img" aria-label="Client portrait"></div>
    <div><b>Laura P</b><small>Office Manager</small></div>
  </div>

  <div class="abs" role="img" aria-label="Warm-toned office interior with wooden floor" style="left:453px;top:2877px;width:613px;height:328px;border-radius:8px;background:linear-gradient(120deg,#3a2a22,#6b4a38 50%,#8a6a55)"></div>
  <div class="stars abs" style="left:480px;top:2903px">
    <svg width="100" height="16" viewBox="0 0 100 16"><g fill="#f5b400"><use href="#st"/><use href="#st" x="20"/><use href="#st" x="40"/><use href="#st" x="60"/><use href="#st" x="80"/></g></svg>
  </div>
  <p class="abs" style="left:480px;top:2938px;width:550px;font-size:19px;line-height:27px;color:#fff">The team provided unparalleled floor care services for our business. Their attention to detail and dedication were evident from day one, helping us maintain the highest standards of cleanliness and appearance in our office. We couldn't be happier with the results.</p>
  <div class="person abs" style="left:480px;top:3098px;width:240px">
    <div class="avatar" role="img" aria-label="Client portrait"></div>
    <div><b>Marco Lenz</b><small>Facility Director</small></div>
  </div>
  <div class="dots abs" style="top:3245px"><span></span><span class="on"></span><span></span></div>
</section>

<!-- Team -->
<section class="team">
  <h2 class="section-title abs" style="top:3380px">The great minds behind our work</h2>
  <div class="member abs" style="left:-110px;top:3470px;width:462px;height:250px">
    <div class="pic" role="img" aria-label="Team member portrait on yellow backdrop" style="background:linear-gradient(135deg,#f3b84a,#e39a2a)"></div>
    <div><h3>Ethan Caldwell</h3><div class="role">Senior Floor Care Specialist</div>
    <p>Ethan has spent over 10 years specializing in commercial flooring solutions, from burnishing to power washing.</p>
    <div class="socials"><span></span><span></span><span></span></div></div>
  </div>
  <div class="member abs" style="left:382px;top:3470px;width:434px;height:310px">
    <div class="pic" role="img" aria-label="Team member portrait on grey backdrop" style="background:linear-gradient(135deg,#8d8a86,#4d4a47)"></div>
    <div><h3>Samuel T. Brooks</h3><div class="role">Founder &amp; CEO</div>
    <p>With over 20 years of experience in the commercial flooring industry, Samuel leads our company with a passion for delivering unmatched floor care services.</p>
    <div class="socials"><span></span><span></span><span></span></div></div>
  </div>
  <div class="member abs" style="left:845px;top:3470px;width:462px;height:250px">
    <div class="pic" role="img" aria-label="Team member portrait on blue backdrop" style="background:linear-gradient(135deg,#5ab0e6,#2a7fc4)"></div>
    <div><h3>Noah Whitfield</h3><div class="role">Lead Technician</div>
    <p>As our lead technician, Noah brings extensive knowledge of advanced cleaning technologies and techniques.</p>
    <div class="socials"><span></span><span></span><span></span></div></div>
  </div>
  <div class="dots abs" style="top:3790px"><span></span><span class="on"></span><span></span></div>
</section>

<!-- Milestones -->
<section class="milestones">
  <p class="eyebrow abs" style="top:3892px">Milestones</p>
  <h2 class="section-title abs" style="top:3912px">Tracking Our Success and Milestones</h2>
  <p class="section-sub abs" style="left:300px;top:3976px;width:600px">Effective progress tracking and milestone setting are critical components of any successful project or personal goal. By systematically monitoring our achievements.</p>
  <div class="stat abs" style="left:78px;top:4070px"><b>22+</b><span>Years of Experience</span></div>
  <div class="vline abs" style="left:405px;top:4055px"></div>
  <div class="stat abs" style="left:406px;top:4070px"><b>70+</b><span>Total Projects</span></div>
  <div class="vline abs" style="left:728px;top:4055px"></div>
  <div class="stat abs" style="left:737px;top:4070px"><b>1K+</b><span>Satisfied Customer</span></div>
</section>

<!-- Contact -->
<section class="contact">
  <h2 class="section-title abs" style="top:4243px">Contact Us</h2>
  <p class="section-sub abs" style="left:0;width:1200px;top:4307px">Whether you're seeking assistance with a product or service.</p>
  <div class="form abs" style="left:133px;top:4370px;width:933px;height:590px"></div>
  <div class="field abs" style="left:175px;top:4410px"><label>Full Name</label><div class="input" style="width:410px">First name</div></div>
  <div class="field abs" style="left:612px;top:4437px"><div class="input" style="width:412px">Last name</div></div>
  <div class="field abs" style="left:175px;top:4497px"><label>Email</label><div class="input" style="width:410px">Enter your email</div></div>
  <div class="field abs" style="left:612px;top:4497px"><label>Phone number</label><div class="input" style="width:412px">Enter 10 digit number</div></div>
  <div class="field abs" style="left:175px;top:4584px"><label>Subject</label><div class="input" style="width:849px">Write subject</div></div>
  <div class="field abs" style="left:175px;top:4671px"><label>Your Message</label><div class="input" style="width:849px;height:100px">Write here...</div></div>
  <span class="btn btn-green abs" style="left:175px;top:4828px;padding:9px 14px;font-size:12px">Send Message
    <svg width="12" height="10" viewBox="0 0 12 10"><path d="M1 5h10M7 1l4 4-4 4" stroke="#fff" fill="none" stroke-width="1.3"/></svg></span>
</section>

<!-- Footer -->
<footer>
  <h2 class="abs" style="left:133px;top:5015px;font-size:38px;font-weight:500;line-height:50px">Let's Work<br>With Experts!</h2>
  <div class="logo abs" style="left:138px;top:5124px">tilebaron<span class="dot"></span></div>
  <p class="abs" style="left:133px;top:5238px;font-size:12px">@2024 tilebaron. All right reserved.</p>
  <div class="abs" style="left:455px;top:5005px;width:1px;height:270px;background:var(--line)"></div>

  <div class="foot-col abs" style="left:500px;top:5000px"><h4>Support</h4><ul><li>FAQ's</li><li>Privacy Policy</li><li>Terms &amp; Conditions</li></ul></div>
  <div class="foot-col abs" style="left:714px;top:5000px"><h4>Company</h4><ul><li>About us</li><li>Blog</li><li>Services</li></ul></div>
  <div class="foot-col abs" style="left:885px;top:5000px"><h4>Contact Info</h4><ul>
    <li><svg width="14" height="14" viewBox="0 0 24 24" fill="none" stroke="#777" stroke-width="2"><path d="M12 22s7-7 7-12a7 7 0 0 0-14 0c0 5 7 12 7 12z"/><circle cx="12" cy="10" r="2.5"/></svg>417, Texas</li>
    <li><svg width="14" height="14" viewBox="0 0 24 24" fill="none" stroke="#777" stroke-width="2"><path d="M5 3h4l2 5-3 2a12 12 0 0 0 6 6l2-3 5 2v4a2 2 0 0 1-2 2A18 18 0 0 1 3 5a2 2 0 0 1 2-2z"/></svg>+1 - 214 - 555 - 0198</li>
    <li><svg width="14" height="14" viewBox="0 0 24 24" fill="none" stroke="#777" stroke-width="2"><rect x="3" y="5" width="18" height="14" rx="2"/><path d="M3 7l9 6 9-6"/></svg>hello@tilebaron.org</li>
  </ul></div>

  <h4 class="abs" style="left:500px;top:5180px;font-size:22px;font-weight:500">Join our newsletter</h4>
  <div class="abs" style="left:500px;top:5228px;width:566px;height:46px;background:var(--card);border-radius:6px"></div>
  <svg class="abs" style="left:512px;top:5244px" width="16" height="14" viewBox="0 0 24 20" fill="none" stroke="#777" stroke-width="2"><rect x="2" y="2" width="20" height="16" rx="2"/><path d="M2 4l10 7 10-7"/></svg>
  <span class="abs" style="left:545px;top:5245px;font-size:11px;color:var(--muted)">Enter your email</span>
  <span class="btn btn-green abs" style="left:935px;top:5235px;padding:9px 12px;font-size:12px">Book a Free Call</span>
</footer>

</body>
</html>
```